Wedding Invite for Same Sex Marriage

Looking for creative ideas for our wedding invite, then other cards/information to accompany the invite i.e RSVP, Info Card, Wishing Well.We're a same sex male couple. Our thoughts are something along the lines of the Brambly cartoon series. We put something together quickly for our Save The Date attached. These were printed in various bright colours. Don't stick to this design, be creative with the theme.Love to see what ideas you have.

Font styles to use
Sans Serif
Decorative
Script

Colors

Designer to choose colors to be used in the design.

Requirements
Must have
• Standard details of our names, location and time
Nice to have
• Unsure, looking for ideas from a creative crowd. Probably standard print sizes
Should not have
• Traditional, not cutesy cartoon

```html
<!DOCTYPE html>
<html lang="en">
<head>
<meta charset="utf-8">
<title>Wedding Invitation – Lewis Harlow &amp; Daniel Prescot</title>
<link rel="stylesheet" href="https://fonts.googleapis.com/css2?family=Federo&family=Varela+Round&display=swap">
<style>
  :root {
    --ink: #000000;
    --paper: #ffffff;
    --gold: #e0a43a;
    --stripe-gap: 12px;
  }
  html, body {
    margin: 0;
    padding: 0;
    width: 846px;
    height: 1200px;
    overflow: hidden;
    background: var(--paper);
  }
  .invitation {
    position: relative;
    width: 846px;
    height: 1200px;
    background: var(--paper);
    overflow: hidden;
  }
  .stripes {
    position: absolute;
    left: 20px;
    top: 36px;
    width: 806px;
    height: 628px;
    background: repeating-linear-gradient(
      to bottom,
      var(--paper) 0,
      var(--paper) calc(var(--stripe-gap) - 2px),
      var(--ink) calc(var(--stripe-gap) - 2px),
      var(--ink) var(--stripe-gap)
    );
  }
  .portrait {
    position: absolute;
    left: 170px;
    top: 66px;
    width: 525px;
    height: 598px;
    background: linear-gradient(to bottom, #1a1a1a, var(--ink));
    border-radius: 140px 140px 0 0;
  }
  .lower-band {
    position: absolute;
    left: 0;
    top: 664px;
    width: 846px;
    height: 536px;
    background: var(--ink);
  }
  .frame {
    position: absolute;
    left: 20px;
    top: 36px;
    width: 806px;
    height: 1140px;
    box-sizing: border-box;
    border: 3px solid var(--gold);
    pointer-events: none;
  }
  .details {
    position: absolute;
    left: 0;
    top: 700px;
    width: 846px;
    text-align: center;
    color: var(--paper);
  }
  .couple {
    margin: 0;
    font-family: "Federo", sans-serif;
    font-weight: 400;
    font-size: 58px;
    line-height: 64px;
    letter-spacing: 2px;
    text-transform: uppercase;
  }
  .couple .amp {
    display: block;
    font-size: 54px;
    line-height: 62px;
  }
  .invite-line {
    margin: 14px 0 0;
    font-family: "Varela Round", sans-serif;
    font-size: 28px;
    letter-spacing: 1px;
  }
  .when {
    margin: 34px 0 0;
    font-family: "Varela Round", sans-serif;
    font-size: 29px;
    line-height: 42px;
    letter-spacing: 1px;
  }
  .where {
    margin: 28px 0 0;
    font-family: "Varela Round", sans-serif;
    font-size: 31px;
    letter-spacing: 1px;
  }
</style>
</head>
<body>
  <main class="invitation">
    <div class="stripes"></div>
    <div class="portrait" role="img" aria-label="Black silhouettes of the two grooms in tuxedos and bow ties, standing back to back"></div>
    <div class="lower-band"></div>
    <div class="frame"></div>

    <section class="details">
      <h1 class="couple">
        Lewis Harlow
        <span class="amp">&amp;</span>
        Daniel Prescot
      </h1>
      <p class="invite-line">Invite you to celebrate their wedding</p>
      <p class="when">00.00.00<br>at 00 PM</p>
      <p class="where">Location</p>
    </section>
  </main>
</body>
</html>
```